TALBRIDGE ELEVATOR CORP

LOOKING FOR BLACK MATTE BACKGROUND WITH GLOSS DESIGN
NEED RAISED UV ON LOGO AND LETTERING , WITH ROUNDED CORNERS AND COLORED EDGES ( FLOURECENT BLUE)

```html
<!DOCTYPE html>
<html lang="en">
<head>
<meta charset="utf-8">
<title>Talbridge Elevator Corp – Business Card</title>
<link rel="stylesheet" href="https://fonts.googleapis.com/css2?family=Tinos:wght@400&display=swap">
<style>
  :root{
    --page:#ffffff;
    --card:#1b1b1b;
    --green:#7dc242;
    --blue:#1a7fd4;
    --white:#f4f4f4;
    --serif:"Tinos","Times New Roman",serif;
  }
  *{margin:0;padding:0;box-sizing:border-box}
  html,body{width:1200px;height:1200px;overflow:hidden;background:var(--page)}
  .sheet{position:relative;width:1200px;height:1200px}
  .card{position:absolute;left:150px;width:900px;height:529px;background:var(--card);border-radius:18px;overflow:hidden;font-family:var(--serif);font-weight:400}
  .card--front{top:50px}
  .card--back{top:621px}
  .card__curve{position:absolute;left:0;top:0;width:900px;height:529px}

  .holder{position:absolute;top:56px;left:0;width:900px;text-align:center}
  .holder__name{display:inline-block;color:var(--green);font-size:50px;font-weight:400;line-height:1;border-bottom:2px solid var(--green);padding-bottom:1px;letter-spacing:.5px}
  .holder__role{color:var(--blue);font-size:18px;line-height:23px;margin-top:6px}
  .address{position:absolute;top:217px;left:157px;color:var(--white);font-size:22px;letter-spacing:.3px}

  .contacts{position:absolute;top:308px;left:157px;list-style:none}
  .contacts li{display:flex;align-items:center;height:34px;margin-bottom:14px;color:var(--blue);font-size:26px;line-height:1}
  .contacts .icon{width:32px;height:32px;margin-right:14px;flex:none}

  .mini-mark{position:absolute;left:799px;top:437px;width:68px;text-align:center}
  .mini-mark__dot{width:56px;height:56px;margin:0 auto;border-radius:50%;background:var(--blue)}
  .mini-mark__est{color:var(--white);font-size:13px;margin-top:3px}

  .brand-mark{position:absolute;left:330px;top:63px;width:240px;height:194px;border-radius:50%;background:var(--blue)}
  .wordmark{position:absolute;top:352px;left:0;width:900px;text-align:center;color:var(--blue);font-size:40px;font-weight:400;line-height:1;letter-spacing:.5px}
  .tagline{position:absolute;top:399px;left:0;width:900px;display:flex;justify-content:center;align-items:center;color:var(--green);font-size:29px;line-height:1;letter-spacing:.5px}
  .tagline::before,.tagline::after{content:"";width:80px;height:2px;background:var(--green);margin:0 14px}
</style>
</head>
<body>
<main class="sheet">

  <section class="card card--front" aria-label="Card front">
    <svg class="card__curve" viewBox="0 0 900 529" aria-hidden="true">
      <path d="M0 267 C 250 236, 520 246, 900 275" fill="none" stroke="var(--green)" stroke-width="5"/>
    </svg>
    <header class="holder">
      <h1 class="holder__name">DANIEL FERROW</h1>
      <p class="holder__role">TALBRIDGE ELEVATOR CORP.<br>PRESIDENT</p>
    </header>
    <p class="address">2270 HARLOW AVENUE , BRONX, NY 10461</p>
    <ul class="contacts">
      <li>
        <svg class="icon" viewBox="0 0 32 32" aria-hidden="true"><circle cx="16" cy="16" r="14" fill="none" stroke="var(--green)" stroke-width="2"/><path d="M10 9 l4 -1 2 5 -2 2 c1 2 3 4 5 5 l2 -2 5 2 -1 4 c-8 0 -15 -7 -15 -15z" fill="var(--green)"/></svg>
        <span>516-555-0142</span>
      </li>
      <li>
        <svg class="icon" viewBox="0 0 32 32" aria-hidden="true"><circle cx="16" cy="16" r="14" fill="none" stroke="var(--green)" stroke-width="2"/><rect x="8" y="11" width="16" height="11" fill="none" stroke="var(--green)" stroke-width="1.6"/><path d="M8 11 l8 6 8 -6 M8 22 l6 -5 M24 22 l-6 -5" fill="none" stroke="var(--green)" stroke-width="1.4"/></svg>
        <span>TALBRIDGEELEVATOR.COM</span>
      </li>
      <li>
        <svg class="icon" viewBox="0 0 32 32" aria-hidden="true"><circle cx="16" cy="16" r="14" fill="none" stroke="var(--green)" stroke-width="2"/><circle cx="16" cy="16" r="8" fill="none" stroke="var(--green)" stroke-width="1.6"/><ellipse cx="16" cy="16" rx="3.5" ry="8" fill="none" stroke="var(--green)" stroke-width="1.4"/><path d="M8 16 h16 M9.5 12 h13 M9.5 20 h13" stroke="var(--green)" stroke-width="1.2"/></svg>
        <span>TALBRIDGE@MAILBOX.COM</span>
      </li>
    </ul>
    <div class="mini-mark">
      <div class="mini-mark__dot"></div>
      <p class="mini-mark__est">EST 1978</p>
    </div>
  </section>

  <section class="card card--back" aria-label="Card back">
    <div class="brand-mark"></div>
    <h2 class="wordmark">TALBRIDGE ELEVATOR CORP</h2>
    <p class="tagline">ELEVATOR SERVICES</p>
  </section>

</main>
</body>
</html>
```